Business card design for Plumbing and Gas fitting company

We need a business card design for our plumbing and gas fitting company using the company logo and director details. Design should be modern and eye-catching however kept reasonably simple. This design should be targeted at commercial businesses/work so professionalism is key.

Target Market(s)

Commercial/business

Industry/Entity Type

Plumbing

Contact Information for Business Card

Warwick Tane
Director
027 815 0937
warwick@harbourlinepipeworks.example
PO Box 8716
Marlow Ridge 4482

Font styles to use
Sans Serif

Requirements
Must have
• Logo
• Modern
• Kept simple
Nice to have
• Colour scheme based around logo

```html
<!DOCTYPE html>
<html lang="en">
<head>
<meta charset="utf-8">
<title>Harbourline Pipeworks – Business Card</title>
<link rel="stylesheet" href="https://fonts.googleapis.com/css2?family=Open+Sans:wght@400;600;700&display=swap">
<style>
  :root {
    --stage: #000000;
    --card-white: #ffffff;
    --brand-blue: #0a6fb9;
    --brand-blue-deep: #0866ab;
    --brand-orange: #e87a2e;
    --ink: #2a2a2a;
  }
  * { margin: 0; padding: 0; box-sizing: border-box; }
  html, body {
    width: 1200px; height: 900px; overflow: hidden;
    background: var(--stage);
    font-family: "Open Sans", Arial, sans-serif;
  }
  .card {
    position: absolute;
    width: 477px; height: 293px;
    overflow: hidden;
  }
  .card-front {
    left: 116px; top: 275px;
    background: var(--card-white);
    border-radius: 0 46px 0 46px;
  }
  .card-back {
    left: 622px; top: 276px;
    background: var(--brand-blue);
    border-radius: 46px 0 46px 0;
  }
  .front-waves { position: absolute; left: 0; top: 0; width: 477px; height: 293px; }
  .brand-mark {
    position: absolute; left: 26px; top: 96px;
    display: flex; align-items: center; gap: 7px;
    font-weight: 700; font-size: 16px; color: var(--brand-blue);
  }
  .brand-dot {
    width: 12px; height: 12px; border-radius: 50%;
    background: var(--brand-blue);
  }
  .contact {
    position: absolute; right: 24px; top: 50px;
    text-align: right; color: var(--ink);
  }
  .person-name {
    font-size: 17px; font-weight: 600; letter-spacing: 0.4px;
    color: var(--brand-blue); line-height: 24px;
  }
  .person-name .surname { color: var(--brand-orange); }
  .person-role { font-size: 13px; line-height: 18px; }
  .contact-line {
    display: flex; justify-content: flex-end; align-items: flex-start;
    gap: 9px; font-size: 13px; line-height: 17px;
  }
  .contact-phone { margin-top: 26px; }
  .contact-post { margin-top: 6px; }
  .contact-line svg { flex: none; margin-top: 2px; }
  .email {
    position: absolute; left: 134px; top: 252px;
    font-size: 13px; color: var(--card-white);
  }
  .back-pattern {
    position: absolute; inset: 0;
    background: linear-gradient(180deg, var(--brand-blue) 0%, var(--brand-blue-deep) 100%);
  }
  .back-brand {
    position: absolute; left: 0; right: 0; top: 164px;
    display: flex; justify-content: center; align-items: center; gap: 10px;
    font-weight: 700; font-size: 26px; color: var(--card-white);
  }
  .back-brand .brand-dot { width: 18px; height: 18px; background: var(--card-white); }
</style>
</head>
<body>
  <section class="card card-front" aria-label="Business card front">
    <svg class="front-waves" viewBox="0 0 477 293" aria-hidden="true">
      <path d="M0,203 C70,168 200,165 405,232 C250,200 110,206 10,266 L0,256 Z" fill="var(--brand-orange)"/>
      <path d="M40,293 C80,240 180,214 280,217 C370,220 430,246 477,243 L477,293 Z" fill="var(--brand-blue)"/>
    </svg>

    <div class="brand-mark"><span class="brand-dot"></span>Harbourline Pipeworks</div>

    <div class="contact">
      <p class="person-name">WARWICK <span class="surname">TANE</span></p>
      <p class="person-role">Director</p>
      <p class="contact-line contact-phone">027 815 0937
        <svg width="10" height="11" viewBox="0 0 24 24" aria-hidden="true"><path fill="var(--brand-blue)" d="M6.6 10.8a15.1 15.1 0 0 0 6.6 6.6l2.2-2.2a1 1 0 0 1 1-.25 11.4 11.4 0 0 0 3.6.57 1 1 0 0 1 1 1V20a1 1 0 0 1-1 1A17 17 0 0 1 3 4a1 1 0 0 1 1-1h3.5a1 1 0 0 1 1 1c0 1.25.2 2.45.57 3.57a1 1 0 0 1-.25 1z"/></svg>
      </p>
      <p class="contact-line contact-post"><span>PO Box 8716<br>Marlow Ridge 4482</span>
        <svg width="10" height="14" viewBox="0 0 24 32" aria-hidden="true"><path fill="var(--brand-blue)" d="M12 0C5.4 0 0 5.4 0 12c0 9 12 20 12 20s12-11 12-20C24 5.4 18.6 0 12 0zm0 17a5 5 0 1 1 0-10 5 5 0 0 1 0 10z"/></svg>
      </p>
    </div>

    <p class="email">warwick@harbourlinepipeworks.example</p>
  </section>

  <section class="card card-back" aria-label="Business card back">
    <div class="back-pattern" role="img" aria-label="Repeating pattern of small flame motifs in a lighter blue"></div>
    <div class="back-brand"><span class="brand-dot"></span>Harbourline Pipeworks</div>
  </section>
</body>
</html>
```